"The Summit Hour Radio Program" needs 3 banner ad designs

I am seeking the design and creation of 3 differently-designed ”banner ads.” I want them to look as though there is a relation between designs but I don't want them to look the same.
While compatibility is desired, that desire should not be interpreted as sameness.

I need a series of banner ads to be a supplement and a complement to
"The Summit Hour"'s main banner ad page and accompanying site.
http://www.qorvalnet.org/

I am looking for high quality, creative capturing of banner ads that focus on three topic areas, namely, my:

1. Leadership Coaching Program –
“Growth Pathway Mentoring Method™”

2. Training program – “The Craft of a Steady Captain”

and

3. Speaker Interest & Availability banner ad.

It is desired that each banner, and the banners collectively, complement and fit in with the look and feel of the existing, principal banner and the show’s vision and mission. (in the attachment, I have included a copy of this banner for your information).

The final design should commit experience, competence, depth and reliability.

To provide a bit of context for this request, I have included the show's vision and mission statement as well as a brief description of my perspective on each banner ad.

I will of course, provide the winner all of the information, documents, graphic depictions, etc that I have available (during the handover stage) that will enable them to create quality products.

In addition, each banner ad should be delivered as JPEG files in dimensions 728 pixel wide and 90 pixels high each. The following fonts: Trajan Pro Regular or Thomas Condensed Regular are the desired fonts.

The task summary: Design 3 banner ads as described below:

1. Leadership Coaching Program – Growth Pathway Mentoring Method™
My coaching program has a formal structure that has an existing graphic capturing of leadership coaching that that would/should be incorporated in the ad.

2. Training program – The Craft of a Steady Captain
The skills training program description I have included as noted below; it is a program that can also be licensed for use by customers who would wish to use it in their organization. In addition to the creative thinking of graphics artists, it would probably be useful to view the home page graphic at www.trm8k.com. This image might be useful in enhancing the banner ad graphic.

3. Speaking Interest – Availability
Have been and desire using this banner to communicate my interest in generating value and availability as a speaker.

-Vision-
“The Summit Hour”
Shaping Tomorrow via Steady Guidance
*is a powerfully engaging platform for great conversations about leadership and leadership learning.

-Mission-
Build a community of listeners who are informed and enthusiastically engaged with the host and the show’s goal of improving the quality of leadership wherever listeners are living and leading.

Leadership Coaching Banner Ad* = *Growth Pathway Mentoring Method*

for use in designing the Book Ad – The Craft of a Steady Captain:
Turning Into Someone a Team Trusts Gladly*

Concepts Summary *this information is for the design of the banner ad for
the Skills Training Course. It includes quotes that could be excerpted to
include in the banner ad*

-> Picture of book for Craft of a Steady Captain Training Program – *this is additional information for the use in designing the Training program banner ad

You can find the other attachments useful. Please have a look.
I welcome all your creative and original designs. Remember, these are 3 different-looking banner ads - though related in some way.

Project Deadline Extended Reason: The current designs have not included enough variety and creativity. While I am desirous of compatibility of the ad renditions with the central image, I am not interpreting compatibility with sameness of looking to see the same image in each banner ad. I rather think the image differentiation promotes both interest and distinction between the products of book, leadership coaching, speaking, etc. Same image embedded in each banner ad doesn't provide the variety that I think both distinguishes and draws interest. In this regard, most of the current examples include the same pictorial images across designs and the use of just words vs. images from among those provided, As an example a picture of my book on the book banner ad seems more impactful than merely using the words book on the ad for the book; and the picture of a speaker vs. Speaker Availability.I hope this feedback is helpful . Regards,Wilfred Added Saturday, June 3, 2017

Target Market(s)

Online Radio Listeners Can Visit SoundHarbor.com for examples - Will be broadcast on the Business Network

Industry/Entity Type

Business Consultant

Colors

Designer to choose colors to be used in the design.

Requirements
Should not have
• Anything that doesn't speak to the characteristics noted at the end of the summary provided in the description above

```html
<!DOCTYPE html>
<html lang="en">
<head>
<meta charset="utf-8">
<title>Wilfred E. Hartwell – Banner Ads</title>
<link rel="stylesheet" href="https://fonts.googleapis.com/css2?family=Cinzel:wght@400;500&display=swap">
<style>
  :root {
    --stage: #000000;
    --peach: #fbe0c2;
    --peach-light: #fff3e6;
    --headline-red: #d9141b;
    --ink: #1a1a1a;
    --bubble: #ffffff;
    --portrait-top: #e9d7c4;
    --portrait-bottom: #3b3f4a;
    --steps-tone: #c9d3dc;
    --road-tone: #4a4d52;
    --figure-tone: #e4e4e4;
  }
  * { margin: 0; padding: 0; box-sizing: border-box; }
  html, body { width: 1200px; height: 902px; overflow: hidden; background: var(--stage); }
  .canvas { position: relative; width: 1200px; height: 902px; }

  .banner {
    position: absolute;
    left: 86px;
    width: 1028px;
    height: 127px;
    overflow: hidden;
    background: linear-gradient(90deg, var(--peach) 0%, var(--peach-light) 55%, var(--peach) 100%);
    font-family: "Cinzel", serif;
  }
  .banner--coaching { top: 191px; }
  .banner--training { top: 391px; }
  .banner--speaking { top: 597px; }

  .portrait {
    position: absolute;
    right: 0; top: 0;
    width: 154px; height: 127px;
    background: linear-gradient(180deg, var(--portrait-top) 0%, #c9a98c 45%, var(--portrait-bottom) 100%);
  }
  .art { position: absolute; left: 0; top: 0; height: 127px; }
  .art--steps { width: 148px; background: linear-gradient(135deg, #f2f4f6 0%, var(--steps-tone) 60%, #b9222a 100%); }
  .art--road { width: 190px; background: linear-gradient(90deg, var(--road-tone) 0%, #6c6f74 60%, rgba(251,224,194,0) 100%); }
  .art--figure { width: 140px; background: radial-gradient(ellipse at 45% 55%, var(--figure-tone) 0%, rgba(251,224,194,0) 70%); }

  .headline {
    position: absolute;
    color: var(--headline-red);
    font-weight: 500;
    letter-spacing: 1px;
    white-space: nowrap;
    text-transform: uppercase;
  }
  .subline {
    position: absolute;
    color: var(--ink);
    white-space: nowrap;
    text-transform: uppercase;
    letter-spacing: 0.5px;
  }
  .signature {
    position: absolute;
    right: 186px;
    color: var(--ink);
    font-size: 11px;
    font-weight: 500;
    letter-spacing: 0.5px;
    text-transform: uppercase;
    white-space: nowrap;
  }

  .banner--coaching .headline { left: 219px; top: 12px; font-size: 31px; }
  .banner--coaching .subline { left: 218px; top: 56px; font-size: 19px; }
  .banner--coaching .signature { top: 100px; }
  .tm { font-size: 8px; vertical-align: super; }

  .banner--training .subline { left: 223px; top: 18px; font-size: 20px; }
  .banner--training .headline { left: 192px; top: 42px; font-size: 33px; }
  .banner--training .signature { top: 100px; }

  .bubble { position: absolute; left: 110px; top: 0; width: 830px; height: 92px; }
  .banner--speaking .headline { left: 211px; top: 26px; font-size: 31px; }
  .banner--speaking .signature { top: 100px; }
</style>
</head>
<body>
<main class="canvas">

  <section class="banner banner--coaching">
    <div class="art art--steps" role="img" aria-label="Illustration of a leader figure standing on a red arrow ahead of a line of followers"></div>
    <h2 class="headline">Leadership Coaching Program</h2>
    <p class="subline">Growth Pathway Mentoring Method<span class="tm">™</span></p>
    <p class="signature">Wilfred E. Hartwell</p>
    <div class="portrait" role="img" aria-label="Portrait photograph of the host in a suit"></div>
  </section>

  <section class="banner banner--training">
    <div class="art art--road" role="img" aria-label="Illustration of a road with white arrows and one red arrow leading forward"></div>
    <p class="subline">Training Program</p>
    <h2 class="headline">The Craft of a Steady Captain</h2>
    <p class="signature">Wilfred E. Hartwell</p>
    <div class="portrait" role="img" aria-label="Portrait photograph of the host in a suit"></div>
  </section>

  <section class="banner banner--speaking">
    <div class="art art--figure" role="img" aria-label="Illustration of a presenter figure gesturing toward a speech bubble"></div>
    <svg class="bubble" viewBox="0 0 830 92" aria-hidden="true">
      <path d="M140 0 H770 A45 45 0 0 1 770 90 H200 Q150 90 140 70 L0 66 L132 58 Q125 40 140 0 Z" fill="var(--bubble)"/>
    </svg>
    <h2 class="headline">Speaking Interest &amp; Availability</h2>
    <p class="signature">Wilfred E. Hartwell</p>
    <div class="portrait" role="img" aria-label="Portrait photograph of the host in a suit"></div>
  </section>

</main>
</body>
</html>
```